GRAPHIC DESIGN FOR RESTAURANT MENU FOR HEALTHY RESTAURANT

I am looking for a graphic design for our menu displayed on a TV screen. Please ensure the file will fit on a TV screen nicely. We are looking for a clean design , with the following items. We would also like to include a couple of photos.
Breakfast:
Protein Chocolate Chip Pancakes - $12.95
Dawn Hustle Burrito- $11.95
Hearty Harvest Omelette - $12.95
Lunch
Butter Chicken - $13.95
Chicken Quesadilla - $13.45
Coconut Garlic Shrimp - $15.95
Goat Cheese Stuffed Chicken - $14.95
Chipotle Steak Wrap - $12.95
Turkey Meatball Fettuccini - $13.45
Chicken Alfredo - $13.45
Chicken Parmesan - $13.95
Pesto Chicken Pasta - $13.45
Steak Bite and Green Stir Fry - $13.45
Asian Chicken Teriyaki - $13.45
Please include our logo

```html
<!DOCTYPE html>
<html lang="en">
<head>
<meta charset="utf-8">
<title>Verdant Menu Board</title>
<link rel="stylesheet" href="https://fonts.googleapis.com/css2?family=Montserrat:wght@500;600;700;800&display=swap">
<style>
  :root {
    --board-black: #000000;
    --leaf-green: #8cc02a;
    --text-white: #ffffff;
    --text-muted: #a7a7a7;
  }
  html, body { margin: 0; padding: 0; overflow: hidden; background: var(--board-black); }
  .menu-board {
    position: relative; width: 1200px; height: 752px; overflow: hidden;
    background: var(--board-black); font-family: 'Montserrat', sans-serif; color: var(--text-white);
  }
  .side-band {
    position: absolute; top: 0; background: var(--leaf-green);
    display: flex; flex-direction: column; align-items: center;
    font-weight: 800; color: var(--text-white); box-sizing: border-box;
  }
  .side-band--breakfast { left: 0; width: 98px; height: 620px; font-size: 50px; padding-top: 36px; line-height: 59px; }
  .side-band--lunch { right: 0; width: 97px; height: 752px; font-size: 50px; padding-top: 126px; line-height: 97px; }
  .vine { position: absolute; left: 571px; top: 0; width: 4px; height: 752px; background: var(--leaf-green); }
  .photo { position: absolute; border-radius: 6px; }
  .photo--omelette { left: 636px; top: 8px; width: 462px; height: 232px; background: radial-gradient(ellipse at 50% 55%, #e7a548 0%, #d89a45 35%, #eaeaea 62%, #cfcfcf 100%); }
  .photo--pancakes { left: 76px; top: 378px; width: 484px; height: 222px; background: radial-gradient(ellipse at 55% 45%, #c99767 0%, #e0c7a2 35%, #eeeeee 62%, #d0d0d0 100%); }
  .breakfast-list { position: absolute; left: 124px; top: 60px; width: 402px; margin: 0; padding: 0; list-style: none; }
  .breakfast-item { display: flex; justify-content: space-between; font-weight: 700; font-size: 23px; line-height: 28px; margin-bottom: 38px; }
  .lunch-list { position: absolute; left: 608px; top: 257px; width: 474px; margin: 0; padding: 0; list-style: none; }
  .lunch-item { display: flex; justify-content: space-between; font-weight: 700; font-size: 20px; height: 44.4px; line-height: 30px; }
  .lunch-item--muted { color: var(--text-muted); font-weight: 600; }
  .brand { position: absolute; left: 124px; top: 664px; display: flex; align-items: center; gap: 14px; font-size: 40px; font-weight: 700; line-height: 48px; color: var(--text-white); }
  .brand-dot { width: 20px; height: 20px; border-radius: 50%; background: var(--leaf-green); }
</style>
</head>
<body>
<main class="menu-board">
  <div class="side-band side-band--breakfast" aria-label="Breakfast">
    <span>B</span><span>R</span><span>E</span><span>A</span><span>K</span><span>F</span><span>A</span><span>S</span><span>T</span>
  </div>
  <div class="side-band side-band--lunch" aria-label="Lunch">
    <span>L</span><span>U</span><span>N</span><span>C</span><span>H</span>
  </div>
  <div class="vine"></div>

  <div class="photo photo--omelette" role="img" aria-label="Omelette with whole grain toast on a white plate"></div>
  <div class="photo photo--pancakes" role="img" aria-label="Stack of chocolate chip pancakes with banana and chocolate drizzle"></div>

  <ul class="breakfast-list">
    <li class="breakfast-item"><span class="name">Protein Chocolate<br>Chip Pancakes</span><span class="price">$12.95</span></li>
    <li class="breakfast-item"><span class="name">Dawn Hustle<br>Burrito</span><span class="price">$11.95</span></li>
    <li class="breakfast-item"><span class="name">Hearty Harvest<br>Omelette</span><span class="price">$12.95</span></li>
  </ul>

  <ul class="lunch-list">
    <li class="lunch-item"><span>Butter Chicken</span><span>$13.95</span></li>
    <li class="lunch-item lunch-item--muted"><span>Chicken Quesadilla</span><span>$13.45</span></li>
    <li class="lunch-item"><span>Coconut Garlic Shrimp</span><span>$15.95</span></li>
    <li class="lunch-item lunch-item--muted"><span>Goat Cheese Stuffed Chicken</span><span>$14.95</span></li>
    <li class="lunch-item"><span>Chipotle Steak Wrap</span><span>$12.95</span></li>
    <li class="lunch-item lunch-item--muted"><span>Turkey Meatball Fettuccini</span><span>$13.45</span></li>
    <li class="lunch-item"><span>Chicken Alfredo</span><span>$13.45</span></li>
    <li class="lunch-item lunch-item--muted"><span>Chicken Parmesan</span><span>$13.95</span></li>
    <li class="lunch-item"><span>Pesto Chicken Pasta</span><span>$13.45</span></li>
    <li class="lunch-item lunch-item--muted"><span>Steak Bite and Green Stir Fry</span><span>$13.45</span></li>
    <li class="lunch-item"><span>Asian Chicken Teriyaki</span><span>$13.45</span></li>
  </ul>

  <div class="brand"><span class="brand-dot"></span><span class="brand-name">Verdant</span></div>
</main>
</body>
</html>
```